Business cards and Stationary | Corvel Music Events

Hello! We need business cards and stationery for a new small business in the music industry. "Corvel is a high-end music agency which provides an unparalleled level of talent and personalized service to the realm entertainment, corporate events, and luxury weddings. Here is where the classical meets the contemporary and we can bring your vision to life.Keeping a steady finger on the pulse of current trends and consistently raising the bar for industry standards, Corvel continues to rise to the forefront of the music industry, providing the utmost professional, high-end, elegant, and engaging entertainment in Australia and World-Wide."

Target Market(s)

Class A. high profile corporate business.

Industry/Entity Type

Entertainment

Contact Information for Business Card

Corvel Music Events

Tessa Holloway
Director | Violinist

Level 7, 41 Marlow Street
Sydney, 2000

Website: www.corvelmusicevents.com
Phone number: 0481 352 604
Email: tessa@corvelmusicevents.com

Font styles to use
Serif
Sans Serif
Script

Colors
feeeee
0355a3
f59296
ffffff

Requirements
Nice to have
• Clean and sophisticated would be perfect.
• If there is a way to include the Instagram without being tacky, that would be awesome
• @corvelmusicevents
• Our website and logo have the following fonts:
• The primary logo is inspired and based on a font called BillionScript but the B is completely hand drawn and the rest is customised a bit to work together cohesively
• Monserrat Light - Is the Music part of the logo and as headers in the site
• Open Sans 300 and 400 (Light or Regular) is used mostly as the body text in the site
• If you want to access the website:
• www.corvelmusicevents.com
• username: client
• password: preview

```html
<!DOCTYPE html>
<html lang="en">
<head>
<meta charset="utf-8">
<title>Corvel Music Events — Business Card</title>
<link rel="stylesheet" href="https://fonts.googleapis.com/css2?family=Parisienne&family=Tinos&family=Montserrat:wght@300&family=Roboto:wght@400&display=swap">
<style>
  :root {
    --backdrop: #2b2b2b;
    --rose: #cd9b9a;
    --rose-deep: #c99593;
    --paper: #ffffff;
    --card-radius: 26px;
  }
  * { box-sizing: border-box; margin: 0; padding: 0; }
  html, body {
    width: 1125px;
    height: 1200px;
    overflow: hidden;
    background: var(--backdrop);
  }
  .canvas {
    position: relative;
    width: 1125px;
    height: 1200px;
  }
  .card {
    position: absolute;
    left: 150px;
    width: 826px;
    height: 471px;
    border-radius: var(--card-radius);
    overflow: hidden;
  }
  .card--front { top: 98px; background: var(--paper); }
  .card--back  { top: 631px; background: var(--rose); }

  /* front: brand half */
  .brand-panel {
    position: absolute;
    left: 0; top: 0;
    width: 435px; height: 100%;
  }
  .brand-name {
    position: absolute;
    left: 206px; top: 237px;
    transform: translate(-50%, -50%);
    font-family: "Montserrat", sans-serif;
    font-weight: 300;
    font-size: 34px;
    letter-spacing: 3px;
    color: var(--rose-deep);
    white-space: nowrap;
  }
  .divider-lines {
    position: absolute;
    left: 0; top: 0;
  }

  /* front: contact half */
  .contact-panel {
    position: absolute;
    left: 435px; top: 0;
    width: 391px; height: 100%;
    background: var(--rose);
    color: var(--paper);
  }
  .contact-text {
    position: absolute;
    left: 47px; top: 96px;
  }
  .person-name {
    font-family: "Parisienne", cursive;
    font-size: 36px;
    line-height: 44px;
  }
  .person-role {
    font-family: "Parisienne", cursive;
    font-size: 24px;
    line-height: 30px;
    margin-top: 2px;
  }
  .address {
    font-family: "Tinos", serif;
    font-size: 19px;
    line-height: 24px;
    margin-top: 17px;
  }
  .contact-list {
    list-style: none;
    font-family: "Tinos", serif;
    font-size: 19px;
    line-height: 26.5px;
    margin-top: 17px;
  }
  .contact-list li {
    display: flex;
    align-items: center;
    gap: 12px;
  }
  .contact-icon {
    width: 18px; height: 18px;
    flex: none;
  }

  /* back */
  .back-name {
    position: absolute;
    left: 50%; top: 236px;
    transform: translate(-50%, -50%);
    font-family: "Montserrat", sans-serif;
    font-weight: 300;
    font-size: 64px;
    letter-spacing: 4px;
    color: var(--paper);
    white-space: nowrap;
  }
  .back-url {
    position: absolute;
    left: 0; right: 0;
    top: 412px;
    text-align: center;
    font-family: "Roboto", sans-serif;
    font-size: 19px;
    letter-spacing: 4.5px;
    color: var(--paper);
  }
</style>
</head>
<body>
<main class="canvas">

  <section class="card card--front" aria-label="Business card front">
    <div class="brand-panel">
      <span class="brand-name">Corvel Music</span>
    </div>

    <svg class="divider-lines" width="826" height="471" viewBox="0 0 826 471" aria-hidden="true">
      <rect x="408" y="115" width="3" height="232" fill="var(--rose)"/>
      <rect x="415" y="62" width="3" height="396" fill="var(--rose)"/>
      <rect x="424" y="0" width="5" height="471" fill="var(--rose)"/>
    </svg>

    <div class="contact-panel">
      <svg width="391" height="471" viewBox="0 0 391 471" aria-hidden="true" style="position:absolute;left:0;top:0">
        <rect x="3" y="42" width="2" height="388" fill="var(--paper)"/>
      </svg>
      <div class="contact-text">
        <p class="person-name">Julian Marsh</p>
        <p class="person-role">CEO/Founder</p>
        <p class="address">Level 7, 41 Marlow Street<br>Sydney, 2000</p>
        <ul class="contact-list">
          <li>
            <svg class="contact-icon" viewBox="0 0 24 24" aria-hidden="true"><path fill="#fff" d="M6.6 10.8a15.1 15.1 0 0 0 6.6 6.6l2.2-2.2c.3-.3.7-.4 1-.2 1.1.4 2.3.6 3.6.6.6 0 1 .4 1 1V20c0 .6-.4 1-1 1A17 17 0 0 1 3 4c0-.6.4-1 1-1h3.5c.6 0 1 .4 1 1 0 1.3.2 2.5.6 3.6.1.3 0 .7-.2 1z"/></svg>
            <span>0481 352 604</span>
          </li>
          <li>
            <svg class="contact-icon" viewBox="0 0 24 24" aria-hidden="true"><rect x="6" y="1.5" width="12" height="21" rx="2" fill="none" stroke="#fff" stroke-width="2"/><circle cx="12" cy="19" r="1.2" fill="#fff"/></svg>
            <span>0481 352 604</span>
          </li>
          <li>
            <svg class="contact-icon" viewBox="0 0 24 24" aria-hidden="true"><rect x="2" y="6" width="20" height="13" fill="#fff"/><path d="M2 6l10 7 10-7" fill="none" stroke="var(--rose)" stroke-width="1.6"/></svg>
            <span>instagram@corvelmusicevents</span>
          </li>
          <li>
            <svg class="contact-icon" viewBox="0 0 24 24" aria-hidden="true"><circle cx="12" cy="12" r="10" fill="#fff"/><path d="M2 12h20M12 2c3 3 3 17 0 20M12 2c-3 3-3 17 0 20" fill="none" stroke="var(--rose)" stroke-width="1.3"/></svg>
            <span>www.corvelmusicevents.com</span>
          </li>
        </ul>
      </div>
    </div>
  </section>

  <section class="card card--back" aria-label="Business card back">
    <span class="back-name">Corvel</span>
    <p class="back-url">www.corvelmusicevents.com</p>
  </section>

</main>
</body>
</html>
```